Quote Cards With TK May 2025 for Instagram

I would like to put these quotes over one of the pictures attached; Instagram (new size: 4:5 (1080 x 1350 pixels) One Quote per picture, and I want the quote to be bold or easy to read as well. I provided a few reference graphics that I really like as examples below. In very small letters at the bottom add @TKBarlowOnline

All of the pictures are attached; you can pick any photo and add one quote to it; but no stock photography

```html
<!DOCTYPE html>
<html lang="en">
<head>
<meta charset="utf-8">
<title>Quote Cards with TK – May 2025</title>
<link href="https://fonts.googleapis.com/css2?family=Bebas+Neue&family=Poppins:wght@700&display=swap" rel="stylesheet">
<style>
  :root {
    --board: #ececec;
    --white: #ffffff;
    --magenta: #d70f6e;
    --magenta-deep: #b80a63;
    --magenta-light: #d84c9e;
    --plum: #8a1a66;
  }
  * { box-sizing: border-box; margin: 0; padding: 0; }
  html, body { width: 1000px; height: 1200px; overflow: hidden; background: var(--board); }
  .board { position: relative; width: 1000px; height: 1200px; }

  .card {
    position: absolute;
    width: 432px;
    height: 540px;
    overflow: hidden;
  }
  .card--flat-tummy   { left: 48px;  top: 40px; }
  .card--stubborn     { left: 520px; top: 40px; }
  .card--tired        { left: 48px;  top: 620px; }
  .card--after-forty  { left: 520px; top: 620px; }

  .card__photo { position: absolute; inset: 0; }
  .card--flat-tummy .card__photo  { background: linear-gradient(160deg, #e0742a 0%, #b21f8f 30%, #6d2a9e 55%, #c0187a 80%, #5a1440 100%); }
  .card--stubborn .card__photo    { background: linear-gradient(170deg, #9aa3b8 0%, #c77098 30%, #d5808f 55%, #e0803a 80%, #b5543a 100%); }
  .card--tired .card__photo       { background: linear-gradient(175deg, #c9cbe8 0%, #d28fb3 35%, #6a2a48 60%, #b04a55 85%, #8a2f3c 100%); }
  .card--after-forty .card__photo { background: linear-gradient(170deg, #2a2c4a 0%, #5b4a58 35%, #7a5440 60%, #d9a15a 80%, #e8a11e 100%); }

  .card__edge {
    position: absolute;
    top: 0; right: 0;
    width: 20px; height: 100%;
    background: var(--plum);
    opacity: 0.55;
  }

  .card__panel {
    position: absolute;
    top: 0; left: 194px;
    width: 218px; height: 100%;
    background: linear-gradient(180deg, var(--magenta) 0%, var(--magenta-deep) 100%);
    color: var(--white);
    text-align: center;
  }
  .card--tired .card__panel { background: linear-gradient(180deg, var(--magenta-light) 0%, #cc2c84 40%, var(--magenta-deep) 100%); }

  .card__headline {
    position: absolute;
    left: -10px; right: -10px;
    top: 92px;
    font-family: "Bebas Neue", "Oswald", sans-serif;
    font-weight: 400;
    font-size: 44px;
    line-height: 40px;
    letter-spacing: 0.5px;
  }
  .card__body {
    position: absolute;
    left: -12px; right: -12px;
    top: 236px;
    font-family: "Poppins", sans-serif;
    font-weight: 700;
    font-size: 16.5px;
    line-height: 24px;
    letter-spacing: 1px;
    text-transform: uppercase;
  }
  .card--tired .card__body { top: 280px; }
  .card--after-forty .card__body { top: 244px; }

  .card__handle {
    position: absolute;
    left: 0; right: 0;
    top: 486px;
    font-family: "Poppins", sans-serif;
    font-weight: 700;
    font-size: 13px;
    letter-spacing: 0.6px;
  }
</style>
</head>
<body>
<main class="board">

  <article class="card card--flat-tummy">
    <div class="card__photo" role="img" aria-label="Photo of TK smiling on a stage in a long pink gown"></div>
    <div class="card__edge"></div>
    <div class="card__panel">
      <h2 class="card__headline">Flat<br>tummy in<br>your 40s?</h2>
      <p class="card__body">It’s still<br>possible!<br>Comment bye<br>belly to get the<br>10 secrets to a<br>flatter tummy</p>
      <p class="card__handle">@TKBarlowOnline</p>
    </div>
  </article>

  <article class="card card--stubborn">
    <div class="card__photo" role="img" aria-label="Photo of TK in a sparkly pink bodysuit beside sunflowers and neon lights"></div>
    <div class="card__edge"></div>
    <div class="card__panel">
      <h2 class="card__headline">That<br>stubborn<br>weight?</h2>
      <p class="card__body">It’s not your<br>fault.<br>Your hormones<br>are to blame and<br>you’re not alone;<br>but there is a fix.</p>
      <p class="card__handle">@TKBarlowOnline</p>
    </div>
  </article>

  <article class="card card--tired">
    <div class="card__photo" role="img" aria-label="Photo of TK in a black outfit on a hillside at sunset"></div>
    <div class="card__edge"></div>
    <div class="card__panel">
      <h2 class="card__headline">Tired.<br>Moody.<br>Stubborn<br>belly fat.</h2>
      <p class="card__body">Your hormones<br>are screaming<br>for help!<br>Let’s fix that.</p>
      <p class="card__handle">@TKBarlowOnline</p>
    </div>
  </article>

  <article class="card card--after-forty">
    <div class="card__photo" role="img" aria-label="Photo of TK courtside in a basketball arena wearing a brown top and black jeans"></div>
    <div class="card__edge"></div>
    <div class="card__panel">
      <h2 class="card__headline">The stubborn<br>belly fat<br>after 40?</h2>
      <p class="card__body">It’s not about<br>calories;<br>it’s about your<br>hormones.<br>Here is the fix!</p>
      <p class="card__handle">@TKBarlowOnline</p>
    </div>
  </article>

</main>
</body>
</html>
```